Website For Custom Home Builder

-Very elegant and simple design as I am a high end custom home builder.
-I build homes $2 million to $10 million range so the website needs to reflect the level of home that I build.
-Attached are photos of homes I have built to use as well as my logo.
-I need final design to be in layered format so my local guy can edit if he needs to.

3 Page Design
1. HomePage:
-logo, some photos,
-“Building beautiful custom homes in Indianapolis for over 20 years”
2. AboutPage:
-Wade Holloran has been building stunning custom homes in the Indianpolis area for over 20 years. As a small boutique building company we only build a handful of homes a year in order to offer our clients the personal attention that their homes deserve. It's this attention to detail that makes our client experience and final product something special and unique.
- family photo
3. ContactPage:
-office photo
-317-552-7190
-wade@whcrafted.com
-415 North Fernmill Rd, Suite 308, Carmel IN 46033

Target Market(s)

Very high end clients looking to build $2 million to $10 million homes.

Industry/Entity Type

Residential high end custom home builder/construction

Coding

Coded - Design and coding required

Number of Pages Required

3 page

Requirements
Must have
• Very simple and elegant design that represents the high end homes that I build.
Nice to have
Should not have
• Should NOT have a lot of clutter or be a very busy page from a design perspective.

```html
<!DOCTYPE html>
<html lang="en">
<head>
<meta charset="utf-8">
<title>Wade Holloran Custom Homes</title>
<link rel="stylesheet" href="https://fonts.googleapis.com/css2?family=Mulish:wght@400;500;600&family=Roboto+Condensed:wght@700&display=swap">
<style>
:root{
  --brand:#9c4709;
  --brand-dark:#7a3605;
  --ink:#141414;
  --ink-soft:#2b2b2b;
  --hero-bg:#f4f3f1;
  --white:#ffffff;
  --muted:#c9c9cc;
}
*{box-sizing:border-box;margin:0;padding:0}
html,body{width:1200px;height:2602px;overflow:hidden}
body{font-family:"Mulish",sans-serif;color:var(--ink);background:var(--white);position:relative}
.page{position:relative;width:1200px;height:2602px;overflow:hidden}

/* hero */
.hero{position:absolute;left:0;top:0;width:1200px;height:706px;
  background:linear-gradient(180deg,#f1f0ee 0%,#f6f5f3 60%,#f7f7f6 100%)}
.hero-glow{position:absolute;right:0;top:0;width:560px;height:600px;
  background:radial-gradient(ellipse at 70% 40%,rgba(200,196,190,.35),rgba(255,255,255,0) 70%)}
.brand{position:absolute;left:140px;top:58px;display:flex;align-items:center;gap:10px}
.brand-mark{width:14px;height:14px;background:var(--brand)}
.brand-name{font-family:"Mulish",sans-serif;font-weight:600;font-size:24px;color:var(--ink);letter-spacing:.5px}
.nav{position:absolute;top:34px;right:150px;display:flex;align-items:center;font-size:15px;font-weight:500}
.nav a{color:var(--ink);text-decoration:none;margin-left:22px}
.nav a.active{color:var(--brand);border-bottom:2px solid var(--brand);padding-bottom:3px}
.nav .divider{width:1px;height:44px;background:#bdbdbd;margin:0 14px 0 24px}
.nav .phone{display:flex;align-items:center;gap:10px;color:var(--brand);font-weight:600;font-size:16px}
.hero-kicker{position:absolute;left:142px;top:218px;font-size:25px;font-weight:600;color:var(--ink)}
.hero-title{position:absolute;left:142px;top:250px;font-family:"Roboto Condensed",sans-serif;font-weight:700;font-size:52px;line-height:64px;color:var(--ink)}
.btn{position:absolute;display:flex;align-items:center;justify-content:center;gap:12px;height:46px;background:var(--brand);color:var(--white);font-size:16px;font-weight:600;letter-spacing:.3px;text-decoration:none}
.btn-hero{left:142px;top:462px;width:352px}
.hero-photo{position:absolute;left:612px;top:128px;width:430px;height:422px;
  background:linear-gradient(180deg,#e9a25a 0%,#b9794a 30%,#6a5a4a 55%,#3e6b8c 72%,#3f6a2a 100%)}
.chevron{position:absolute;left:0;top:610px;width:1200px;height:100px}

/* gallery */
.gallery-head{position:absolute;left:0;top:738px;width:1200px;text-align:center}
.gallery-title{font-size:25px;font-weight:500;color:var(--ink)}
.rule{width:54px;height:2px;background:var(--brand);margin:14px auto 0}
.gallery-intro{position:absolute;left:230px;top:796px;width:740px;text-align:center;font-size:12px;line-height:21px;color:var(--ink-soft)}
.grid{position:absolute;left:141px;top:872px;display:grid;grid-template-columns:repeat(3,300px);grid-auto-rows:229px;column-gap:10px;row-gap:19px}
.tile{width:300px;height:229px}
.t-pool-night{background:linear-gradient(180deg,#6e5440 0%,#c08a4a 45%,#1f4fb0 80%,#0d2f8a 100%)}
.t-bar{background:linear-gradient(180deg,#f3f3f2 0%,#a67b54 50%,#d8c6ad 100%)}
.t-living-bright{background:linear-gradient(180deg,#f4f3f1 0%,#b5a797 40%,#dccbb3 100%)}
.t-living-stone{background:linear-gradient(180deg,#ede9e4 0%,#a8998a 45%,#d4c2a7 100%)}
.t-pool-dusk{background:linear-gradient(180deg,#d89a5a 0%,#5d5a4a 40%,#2f6ca0 65%,#3b5a24 100%)}
.t-kitchen-wood{background:linear-gradient(180deg,#eeeeec 0%,#8a5a34 55%,#d9c7ab 100%)}
.t-stair{background:linear-gradient(135deg,#f1f0ee 0%,#c9a46e 50%,#3a3a3a 100%)}
.t-rec-room{background:linear-gradient(180deg,#e9e9e8 0%,#6a5a4c 50%,#c9c9c6 100%)}
.t-rear-facade{background:linear-gradient(180deg,#c98e5a 0%,#5b3f2d 45%,#c9812f 65%,#3a5a22 100%)}
.t-lounge{background:linear-gradient(180deg,#f2f2f0 0%,#8c8d8f 50%,#bcbcbc 100%)}
.t-front-facade{background:linear-gradient(180deg,#e8a765 0%,#6b5b4e 50%,#b78a4e 70%,#45642a 100%)}
.t-kitchen-white{background:linear-gradient(180deg,#f4f4f3 0%,#dcd8d2 50%,#8a5232 100%)}
.btn-gallery{left:423px;top:1893px;width:352px}

/* contact block */
.contact{position:absolute;left:142px;top:2200px;width:330px}
.contact-title{font-size:19px;font-weight:600;color:var(--ink)}
.contact-lead{font-size:12px;line-height:21px;margin-top:6px;color:var(--ink-soft)}
.contact-row{display:flex;gap:12px;margin-top:18px;font-size:13px;line-height:19px;color:var(--ink)}
.contact-row svg{flex:none;margin-top:2px}
.vertical-name{position:absolute;left:528px;top:2445px;transform:rotate(-90deg);transform-origin:0 0;
  font-size:38px;font-weight:400;color:var(--muted);letter-spacing:2px;white-space:nowrap}
.portrait{position:absolute;left:648px;top:2052px;width:340px;height:504px;border-radius:160px 160px 0 0;
  background:linear-gradient(180deg,#e9e6e2 0%,#c9b8a6 25%,#3b3d42 55%,#2a2c30 100%)}
.footer{position:absolute;left:0;top:2556px;width:1200px;height:46px;background:var(--brand);
  color:var(--white);font-size:12px;display:flex;align-items:center;justify-content:center}
</style>
</head>
<body>
<div class="page">
  <header class="hero">
    <div class="hero-glow"></div>
    <div class="brand"><span class="brand-mark"></span><span class="brand-name">Wade Holloran</span></div>
    <nav class="nav">
      <a href="#" class="active">Home</a>
      <a href="#">About Wade Holloran</a>
      <a href="#">Contact Us</a>
      <span class="divider"></span>
      <span class="phone">
        <svg width="24" height="24" viewBox="0 0 24 24" fill="none" stroke="currentColor" stroke-width="1.5"><path d="M5 3l4 1 1.5 4.5-2.5 1.5a11 11 0 0 0 6 6l1.5-2.5L20 15l1 4-2 2C11 21 3 13 3 5z"/><path d="M14 3a7 7 0 0 1 7 7M14 6a4 4 0 0 1 4 4"/></svg>
        317-552-7190
      </span>
    </nav>
    <p class="hero-kicker">Building Beautiful</p>
    <h1 class="hero-title">Custom Homes<br>In Indianapolis For<br>Over 20 Years</h1>
    <a class="btn btn-hero" href="#">
      <svg width="24" height="24" viewBox="0 0 24 24" fill="none" stroke="currentColor" stroke-width="1.5"><path d="M5 3l4 1 1.5 4.5-2.5 1.5a11 11 0 0 0 6 6l1.5-2.5L20 15l1 4-2 2C11 21 3 13 3 5z"/><path d="M14 3a7 7 0 0 1 7 7M14 6a4 4 0 0 1 4 4"/></svg>
      Contact Us Today 317-552-7190
    </a>
    <div class="hero-photo" role="img" aria-label="Photo of a luxury home's backyard pool at sunset"></div>
    <svg class="chevron" viewBox="0 0 1200 100" preserveAspectRatio="none">
      <polygon points="0,100 600,12 1200,100 1200,91 600,3 0,91" fill="var(--brand)"/>
      <polygon points="0,100 600,12 1200,100" fill="var(--white)"/>
    </svg>
  </header>

  <section class="gallery">
    <div class="gallery-head">
      <h2 class="gallery-title">Work Gallery</h2>
      <div class="rule"></div>
    </div>
    <p class="gallery-intro">We can provide all phases of construction from design to completion. Quis nostrud exerci tation ullamcorper suscipit lobortis nisl ut aliquip ex ea commodo consequat.</p>
    <div class="grid">
      <div class="tile t-pool-night" role="img" aria-label="Photo of a stone home with lit patio and pool at night"></div>
      <div class="tile t-bar" role="img" aria-label="Photo of a wet bar with tall windows and stools"></div>
      <div class="tile t-living-bright" role="img" aria-label="Photo of an open living room with wood beams"></div>
      <div class="tile t-living-stone" role="img" aria-label="Photo of a living room with stone fireplace"></div>
      <div class="tile t-pool-dusk" role="img" aria-label="Photo of a backyard pool at dusk"></div>
      <div class="tile t-kitchen-wood" role="img" aria-label="Photo of a kitchen with wood cabinetry and island"></div>
      <div class="tile t-stair" role="img" aria-label="Photo of an oak staircase with glass railing"></div>
      <div class="tile t-rec-room" role="img" aria-label="Photo of a basement bar and entertainment room"></div>
      <div class="tile t-rear-facade" role="img" aria-label="Photo of a home's rear facade lit at dusk"></div>
      <div class="tile t-lounge" role="img" aria-label="Photo of a lounge with sectional sofa"></div>
      <div class="tile t-front-facade" role="img" aria-label="Photo of a home's front facade at sunset"></div>
      <div class="tile t-kitchen-white" role="img" aria-label="Photo of a white kitchen with brass pendants"></div>
    </div>
    <a class="btn btn-gallery" href="#">
      <svg width="24" height="24" viewBox="0 0 24 24" fill="none" stroke="currentColor" stroke-width="1.5"><path d="M5 3l4 1 1.5 4.5-2.5 1.5a11 11 0 0 0 6 6l1.5-2.5L20 15l1 4-2 2C11 21 3 13 3 5z"/><path d="M14 3a7 7 0 0 1 7 7M14 6a4 4 0 0 1 4 4"/></svg>
      Contact Me Today 317-552-7190
    </a>
  </section>

  <section class="contact">
    <h3 class="contact-title">Very High End Custom Home Builder</h3>
    <p class="contact-lead">We can provide all phases of construction from<br>design to completion.</p>
    <div class="contact-row">
      <svg width="20" height="24" viewBox="0 0 20 24" fill="none" stroke="var(--brand)" stroke-width="1.5"><path d="M10 23s8-8 8-14a8 8 0 0 0-16 0c0 6 8 14 8 14z"/><circle cx="10" cy="9" r="3"/></svg>
      <span>415 North Fernmill Rd, Suite 308<br>Carmel IN 46033</span>
    </div>
    <div class="contact-row">
      <svg width="24" height="24" viewBox="0 0 24 24" fill="none" stroke="var(--brand)" stroke-width="1.5"><path d="M5 3l4 1 1.5 4.5-2.5 1.5a11 11 0 0 0 6 6l1.5-2.5L20 15l1 4-2 2C11 21 3 13 3 5z"/><path d="M14 3a7 7 0 0 1 7 7M14 6a4 4 0 0 1 4 4"/></svg>
      <span>Call Us<br>317-552-7190</span>
    </div>
    <div class="contact-row">
      <svg width="22" height="22" viewBox="0 0 22 22" fill="none" stroke="var(--brand)" stroke-width="1.5"><rect x="1" y="7" width="20" height="14"/><path d="M1 7l10 8 10-8M4 7V2h14v5"/></svg>
      <span>Email Us<br>wade@whcrafted.com</span>
    </div>
  </section>
  <div class="vertical-name">Wade Holloran</div>
  <div class="portrait" role="img" aria-label="Portrait photo of the builder in a suit offering a handshake"></div>

  <footer class="footer">© 2022 Wade Holloran Custom Homes. All Rights Reserved.</footer>
</div>
</body>
</html>
```